Kettlebrook Holdings, LLC. What we do is rehab homes for the purpose of flipping them and also have a rental portfolio as well.

We do not have a logo so that will need to be part of the design process

Would like, if possible to have a house or something with housing or remodeling incorporated in design.

Industry/Entity Type

Rental

Contact Information for Business Card

Dale Varnum
912 thistle Ct.
Fernvale, Il 60000
555-555-0143
Fax 555-555-0178

```html
<!DOCTYPE html>
<html lang="en">
<head>
<meta charset="utf-8">
<title>Kettlebrook Holdings, LLC — Business Card</title>
<link rel="stylesheet" href="https://fonts.googleapis.com/css2?family=Open+Sans:wght@400;700&display=swap">
<style>
  :root {
    --page: #ffffff;
    --card-dark: #121416;
    --card-dark-edge: #050607;
    --card-light: #e6e5e6;
    --card-light-edge: #a9a7a9;
    --teal: #2fb3a6;
    --teal-deep: #0f4a47;
    --text-light: #e9eaea;
    --text-muted: #b9bcbd;
    --rule: #8a8d8e;
  }
  * { margin: 0; padding: 0; box-sizing: border-box; }
  html, body {
    width: 1200px; height: 800px; overflow: hidden;
    background: var(--page);
    font-family: "Open Sans", Arial, sans-serif;
  }
  .canvas {
    width: 1200px; height: 800px;
    display: flex; align-items: center; justify-content: center; gap: 40px;
  }
  .card {
    width: 540px; height: 309px; position: relative; overflow: hidden;
    box-shadow: 0 10px 28px rgba(0,0,0,.25);
  }

  /* Front: contact side */
  .card--front {
    background: radial-gradient(ellipse at 45% 35%, #1d2124 0%, var(--card-dark) 55%, var(--card-dark-edge) 100%);
  }
  .card--front .texture {
    position: absolute; inset: 0;
    background: linear-gradient(160deg, rgba(255,255,255,.04), rgba(0,0,0,.15));
  }
  .brand-mark {
    position: absolute; left: 78px; top: 52px;
    display: flex; align-items: center; gap: 10px;
    color: var(--teal); font-weight: 700; font-size: 20px; letter-spacing: .5px;
  }
  .brand-mark .square { width: 26px; height: 26px; background: var(--teal); }
  .divider {
    position: absolute; left: 40px; top: 108px; width: 300px; height: 1px;
    background: var(--rule);
  }
  .contact { position: absolute; left: 92px; top: 118px; color: var(--text-light); }
  .contact .name { font-weight: 700; font-size: 24px; letter-spacing: .5px; margin-bottom: 6px; }
  .contact .line {
    display: flex; align-items: center; gap: 8px;
    font-size: 14px; color: var(--text-muted); line-height: 22px;
  }
  .contact .line svg { width: 12px; height: 12px; fill: var(--text-muted); flex: none; }
  .accent-stripe {
    position: absolute; left: 0; right: 0; top: 262px; height: 4px;
    background: linear-gradient(90deg, #0b3331, var(--teal) 20%, #9ff0e6 45%, var(--teal-deep) 60%, var(--teal) 80%, #0b3331);
  }

  /* Back: brand side */
  .card--back {
    background: radial-gradient(ellipse at 50% 50%, #ffffff 0%, var(--card-light) 45%, var(--card-light-edge) 100%);
    display: flex; align-items: center; justify-content: center; gap: 14px;
  }
  .card--back .square { width: 40px; height: 40px; background: var(--teal-deep); }
  .card--back .company {
    color: var(--teal-deep); font-weight: 700; font-size: 24px; letter-spacing: .5px;
  }
</style>
</head>
<body>
  <main class="canvas">
    <section class="card card--front" aria-label="Business card front">
      <div class="texture"></div>
      <div class="brand-mark"><span class="square"></span><span>Kettlebrook</span></div>
      <div class="divider"></div>
      <div class="contact">
        <p class="name">Dale Varnum</p>
        <p class="line">
          <svg viewBox="0 0 12 12" aria-hidden="true"><path d="M6 0a4 4 0 0 0-4 4c0 3 4 8 4 8s4-5 4-8a4 4 0 0 0-4-4zm0 5.6A1.6 1.6 0 1 1 6 2.4a1.6 1.6 0 0 1 0 3.2z"/></svg>
          912 thistle Ct. Fernvale, Il 60000
        </p>
        <p class="line">
          <svg viewBox="0 0 12 12" aria-hidden="true"><path d="M2.5 0.5l2 2.5-1.2 1.3a7 7 0 0 0 4.4 4.4l1.3-1.2 2.5 2-1.5 2C5 11.5 0.5 7 0.5 2z"/></svg>
          555-555-0143
        </p>
        <p class="line">
          <svg viewBox="0 0 12 12" aria-hidden="true"><path d="M3 0h5v3H3zM1 4h10v6H9v2H3v-2H1zm3 4v3h4V8z"/></svg>
          555-555-0178
        </p>
      </div>
      <div class="accent-stripe"></div>
    </section>

    <section class="card card--back" aria-label="Business card back">
      <span class="square"></span>
      <span class="company">Kettlebrook Holdings, LLC</span>
    </section>
  </main>
</body>
</html>
```